Visualisation Software brochure

i need a sales brochure for a new visualisation software company called Lumora Scene Studio.
The software has been specifically designed for manufacturers, distributers and retailers in the design / décor / furnishing / building industries. It allows customers can then import unlimited numbers of digital photos of rooms from their own home or take advantage of a library of pre-made photos, and then render different products from your catalogue into that photo to see what the finished look will be.
i have attached:
1) a mock up of the home page of the website
2) example of brochure wording that i have put together (although i am a little unsure about what other words i can add - so any suggestions here would be good)
3) i have attached some examples of other brochures that i like and would like similar designs
I am after a classy brochure used by a large corporate technology company that is given to executives and gives an impression of quality, trustworthiness and innovation.
• the colour blue as per the colours on my website mock up provided in the design brief
• I like simple, smart, clean and uncluttered design
• I like simple, clean and uncluttered design
• I like pictures that fit in with my technology (whether that be home and interior design, mixing virtual world and real world, visualising an idea) rather than basic stock of corporate people
Updates
Target Market(s)
marketing professionals
Industry/Entity Type
Software
Font styles to use
Look and feel
Each slider illustrates characteristics of the customer's brand and the style your logo design should communicate.

```html
<!DOCTYPE html>
<html lang="en">
<head>
<meta charset="utf-8">
<title>Lumora Scene Studio – Sales Brochure Spread</title>
<link rel="stylesheet" href="https://fonts.googleapis.com/css2?family=Open+Sans:wght@400;600;700&display=swap">
<style>
  :root {
    --stage: #e4e4e4;
    --paper: #ffffff;
    --brand-blue: #26479a;
    --accent-blue: #2f7fd0;
    --icon-grey: #4a4a4a;
    --text-grey: #5a5a5a;
    --text-light: #ffffff;
    --photo-warm-a: #e9a24a;
    --photo-warm-b: #c98a52;
    --photo-warm-c: #b7b9c4;
    --photo-office-a: #e8e9ec;
    --photo-office-b: #c9ccd2;
  }
  * { box-sizing: border-box; margin: 0; padding: 0; }
  html, body {
    width: 1200px; height: 800px; overflow: hidden;
    background: var(--stage);
    font-family: "Open Sans", Arial, sans-serif;
  }
  .spread {
    position: absolute; left: 80px; top: 50px;
    width: 1040px; height: 700px;
    display: flex;
    box-shadow: 0 10px 30px rgba(0,0,0,0.18);
  }
  .page { position: relative; width: 520px; height: 700px; background: var(--paper); overflow: hidden; }

  /* Left page */
  .page--left { display: flex; }
  .lifestyle-photo {
    width: 290px; height: 100%;
    background: linear-gradient(170deg, var(--photo-warm-a) 0%, var(--photo-warm-b) 45%, var(--photo-warm-c) 100%);
  }
  .gutter-strip { width: 14px; background: var(--paper); }
  .benefits-column {
    width: 216px; height: 100%;
    background: var(--brand-blue);
    color: var(--text-light);
    padding: 128px 14px 0 14px;
    font-size: 8.2px; line-height: 1.36;
  }
  .benefits-column h3 { font-size: 8.6px; font-weight: 700; margin-bottom: 1px; }
  .benefits-list { list-style: none; margin-bottom: 22px; }
  .benefits-list li { position: relative; padding-left: 7px; }
  .benefits-list li::before { content: "•"; position: absolute; left: 0; }

  /* Right page */
  .office-photo {
    position: absolute; left: 0; top: 0; width: 100%; height: 300px;
    background: linear-gradient(120deg, var(--photo-office-a) 0%, var(--photo-office-b) 100%);
  }
  .section-tab {
    position: absolute; left: 22px; top: 268px;
    height: 28px; width: 150px;
    background: var(--accent-blue); color: var(--text-light);
    font-size: 17px; line-height: 28px; padding-left: 12px;
  }
  .section-band {
    position: absolute; left: 0; top: 298px; width: 490px; height: 34px;
    background: var(--brand-blue); color: var(--text-light);
    font-size: 17px; line-height: 34px; padding-left: 34px;
  }
  .steps {
    position: absolute; left: 28px; top: 380px; width: 470px;
    display: grid; grid-template-columns: 240px 220px; column-gap: 10px;
  }
  .steps__col { display: flex; flex-direction: column; gap: 20px; }
  .step { display: flex; align-items: flex-start; gap: 12px; min-height: 50px; }
  .step__icon {
    flex: none; width: 44px; height: 44px; border-radius: 50%;
    background: var(--icon-grey);
    display: flex; align-items: center; justify-content: center;
  }
  .step__text { font-size: 8.4px; line-height: 1.4; color: var(--text-grey); padding-top: 4px; }
  .steps__closing { font-size: 8.4px; color: var(--text-grey); margin: 6px 0 0 44px; }
</style>
</head>
<body>
<main class="spread">
  <section class="page page--left">
    <div class="lifestyle-photo" role="img" aria-label="Photo from above: a smiling couple lying on a wooden parquet floor beside an open laptop"></div>
    <div class="gutter-strip"></div>
    <div class="benefits-column">
      <h3>Retailer Benefits:</h3>
      <ul class="benefits-list">
        <li>Be the market innovator and leader by combining technology and a dynamic, seamless, integrated and consistent level of customer service across all online, bricks-and-mortar and mobile channels that delivers the big wow factor</li>
        <li>Extend your reach - don't limit your technology footprint by only using Orchard apps - our solution leverages and optimises all mobile devices and desktops (Nimbus OS, Verdant OS, Web). This equates to a larger watershed of customers and more sales</li>
        <li>Increase brand engagement as our bespoke and scalable visualisation application will help customers build a relationship with your company, brand, and products and then share that experience within their social circles</li>
        <li>Understand buyer behaviour by receiving real usage statistics to obtain valuable insight about your customers and conduct trend analysis to determine how your future strategies can further enhance your bottom-line</li>
        <li>Increased sales to further grow your business</li>
        <li>Maximise the exposure of your products by uploading your entire product catalogue into a visualisation software that makes them look real</li>
      </ul>
      <h3>Consumer Benefits:</h3>
      <ul class="benefits-list">
        <li>Reduce your customer's purchase anxiety as they will have the knowledge that the products they are choosing from your range are the right choice</li>
        <li>Greater flexibility in the way they shop by being open 24/7 and being able to engage with your brand when they want and how they want</li>
        <li>Happier customers and hence more sales</li>
        <li>An easy-to-use interface along with guided help and tutorials for those less confident with technology</li>
        <li>Being able to make informed purchasing decisions as they can easily compare a large range of your products at the touch of a computer key</li>
        <li>Improved personalised buying experience by enabling customers to use photos of their own personal spaces and incorporate your products</li>
      </ul>
    </div>
  </section>

  <section class="page page--right">
    <div class="office-photo" role="img" aria-label="Photo of two colleagues at a laptop in a bright white office with a bookshelf"></div>
    <div class="section-tab">Sales process</div>
    <div class="section-band">6 steps to success</div>

    <div class="steps">
      <div class="steps__col">
        <div class="step">
          <div class="step__icon">
            <svg width="24" height="16" viewBox="0 0 24 16"><path d="M6 15h13a4 4 0 0 0 0-8 6 6 0 0 0-11.5-1.5A4.8 4.8 0 0 0 6 15z" fill="#fff"/></svg>
          </div>
          <p class="step__text">1. Leverage the internet and the power of word-of-mouth</p>
        </div>
        <div class="step">
          <div class="step__icon">
            <svg width="22" height="22" viewBox="0 0 22 22"><circle cx="7" cy="7" r="4" fill="none" stroke="#fff" stroke-width="2"/><path d="M10 10l8 8M14 14l2-2M16 16l2-2" stroke="#fff" stroke-width="2" stroke-linecap="round"/></svg>
          </div>
          <p class="step__text">2. Increase interest / desire via the website by seeing how virtualised product placement works – so that's how my house or room will look if I buy those products</p>
        </div>
        <div class="step">
          <div class="step__icon">
            <svg width="24" height="20" viewBox="0 0 24 20"><path d="M2 8h20l-2.5 10h-15z" fill="#fff"/><path d="M7 8l4-6M17 8l-4-6" stroke="#fff" stroke-width="1.8" stroke-linecap="round"/><path d="M8 11v5M12 11v5M16 11v5" stroke="#4a4a4a" stroke-width="1.4"/></svg>
          </div>
          <p class="step__text">3. Combine the virtual and real worlds during an in-store or onsite consultation – virtual walk through your products combined with physical samples</p>
        </div>
      </div>
      <div class="steps__col">
        <div class="step">
          <div class="step__icon">
            <svg width="22" height="22" viewBox="0 0 22 22"><circle cx="11" cy="8" r="5" fill="#fff"/><path d="M3 21a8 6 0 0 1 16 0z" fill="#fff"/><path d="M5 9a6 6 0 0 1 12 0" fill="none" stroke="#fff" stroke-width="1.6"/></svg>
          </div>
          <p class="step__text">4. Sales consultants qualify customer requirements</p>
        </div>
        <div class="step">
          <div class="step__icon">
            <svg width="20" height="22" viewBox="0 0 20 22"><rect x="3" y="1" width="14" height="20" rx="1.5" fill="#fff"/><circle cx="10" cy="10" r="4.5" fill="none" stroke="#4a4a4a" stroke-width="1.4"/><text x="10" y="12.6" font-size="7" font-family="Open Sans, sans-serif" font-weight="700" text-anchor="middle" fill="#4a4a4a">$</text><path d="M6 17h8" stroke="#4a4a4a" stroke-width="1.4"/></svg>
          </div>
          <p class="step__text">5. Trial close by sales consultant – what is required for the customer to purchase</p>
        </div>
        <div class="step">
          <div class="step__icon">
            <svg width="22" height="22" viewBox="0 0 22 22"><rect x="2" y="2" width="13" height="18" rx="1.5" fill="#fff"/><path d="M4.5 7l1.2 1.2L8 6M4.5 12l1.2 1.2L8 11" stroke="#4a4a4a" stroke-width="1.2" fill="none"/><path d="M9.5 7.5h3.5M9.5 12.5h3.5" stroke="#4a4a4a" stroke-width="1.2"/><path d="M19 6l2 2-7 7-2.5.5.5-2.5z" fill="#fff" stroke="#4a4a4a" stroke-width="0.8"/></svg>
          </div>
          <p class="step__text">6. Full sales opportunity close and determine steps to purchase / register</p>
        </div>
        <p class="steps__closing">It all leads to the register.</p>
      </div>
    </div>
  </section>
</main>
</body>
</html>
```